Gift Packaging Beauty Products

I am looking for a gift packaging that can be used for luxurious female beauty products in different sized boxes.

The packaging needs to look like gift already, so people don't even have to wrap it in before giving it to others.

Logo: VELMORINE (see attachment)

Style:
High Class
Trendy Femine
Gift Wrap (see attachment)
Subtle Baroque Patterns/Elements

Colors:
Metallic (Rose) Gold
White

Target Market(s)

Luxurious Female Beauty Products

Industry/Entity Type

Beauty

Font styles to use
Serif
Decorative

Requirements
Must have
• Gift Wrap / Present design
Should not have
• Too busy / too much patterns

```html
<!DOCTYPE html>
<html lang="en">
<head>
<meta charset="utf-8">
<title>VELMORINE Beauty Products – Gift Box</title>
<link href="https://fonts.googleapis.com/css2?family=Playfair+Display:wght@400&display=swap" rel="stylesheet">
<style>
  :root {
    --edge: #0a0a0c;
    --paper: #ebebeb;
    --stripe: #e6cdb2;
    --ink: #2a0d0e;
    --gold-light: #ecc796;
    --gold: #c9874a;
    --gold-deep: #b46f35;
    --red-left: #aa1f25;
    --red-right: #6c2722;
    --white: #ffffff;
  }
  html, body { margin: 0; padding: 0; overflow: hidden; background: var(--edge); }
  .box {
    position: relative;
    width: 919px; height: 1200px;
    background: var(--edge);
    overflow: hidden;
  }
  .box__panel {
    position: absolute; left: 16px; top: 16px; right: 16px; bottom: 16px;
    background:
      repeating-linear-gradient(90deg,
        transparent 0 10px, var(--stripe) 10px 11px,
        transparent 11px 15px, var(--stripe) 15px 16px,
        transparent 16px 28px);
    background-color: var(--paper);
    overflow: hidden;
  }
  .damask {
    position: absolute;
    border-radius: 46% 54% 50% 50% / 40% 45% 55% 60%;
  }
  .damask--upper-left {
    left: 8px; top: 4px; width: 390px; height: 930px;
    background: radial-gradient(ellipse at 45% 40%, rgba(222,180,135,.55), rgba(222,180,135,.25) 60%, rgba(222,180,135,0) 75%);
  }
  .damask--lower-right {
    left: 548px; top: 450px; width: 360px; height: 720px;
    background: radial-gradient(ellipse at 60% 55%, rgba(201,135,74,.85), rgba(226,176,120,.55) 55%, rgba(226,176,120,0) 74%);
  }
  .frame { position: absolute; inset: 0; }
  .badge { position: absolute; inset: 0; }
  .badge__name {
    position: absolute; left: 194px; width: 560px; top: 448px;
    margin: 0; text-align: center;
    font-family: "Playfair Display", Georgia, serif;
    font-weight: 400; font-size: 40px; line-height: 1;
    letter-spacing: 0.5em; text-indent: 0.5em;
    color: var(--white);
  }
  .badge__tagline {
    position: absolute; left: 194px; width: 560px; top: 502px;
    margin: 0; text-align: center;
    font-family: "Playfair Display", Georgia, serif;
    font-size: 17px; line-height: 1;
    letter-spacing: 0.42em; text-indent: 0.42em;
    color: var(--white);
  }
</style>
</head>
<body>
<main class="box">
  <div class="box__panel"></div>

  <div class="damask damask--upper-left" role="img" aria-label="Soft gold baroque damask flourish in the upper left"></div>
  <div class="damask damask--lower-right" role="img" aria-label="Rose gold baroque damask flourish in the lower right"></div>

  <svg class="frame" width="919" height="1200" viewBox="0 0 919 1200" aria-hidden="true">
    <g stroke="var(--ink)" stroke-linecap="round" fill="none">
      <line x1="261" y1="101" x2="672" y2="101" stroke-width="2"/>
      <line x1="300" y1="116" x2="612" y2="116" stroke-width="1.5"/>
      <line x1="85" y1="146" x2="85" y2="489" stroke-width="3"/>
      <line x1="85" y1="810" x2="85" y2="1152" stroke-width="3"/>
      <line x1="841" y1="149" x2="841" y2="483" stroke-width="3"/>
      <line x1="242" y1="1158" x2="612" y2="1158" stroke-width="1.5"/>
      <line x1="107" y1="1176" x2="697" y2="1176" stroke-width="2"/>
    </g>
  </svg>

  <section class="badge" aria-label="VELMORINE beauty products label">
    <svg width="919" height="1200" viewBox="0 0 919 1200" aria-hidden="true">
      <defs>
        <path id="cartouche" d="M337,303 C370,250 420,230 474,230 C528,230 582,250 615,303 L690,303 Q700,351 753,351 Q730,465 753,579 Q700,579 690,618 L615,618 C582,680 528,702 474,702 C420,702 370,680 337,618 L262,618 Q252,579 194,579 Q217,465 194,351 Q252,351 262,303 Z"/>
        <linearGradient id="gold-rim" x1="0" x2="1" y1="0" y2="0">
          <stop offset="0" stop-color="var(--gold)"/>
          <stop offset=".3" stop-color="var(--gold-light)"/>
          <stop offset=".6" stop-color="var(--gold-deep)"/>
          <stop offset="1" stop-color="var(--gold-light)"/>
        </linearGradient>
        <linearGradient id="red-field" x1="0" x2="1" y1="0" y2="0">
          <stop offset="0" stop-color="var(--red-left)"/>
          <stop offset="1" stop-color="var(--red-right)"/>
        </linearGradient>
        <filter id="lift" x="-10%" y="-10%" width="130%" height="130%">
          <feDropShadow dx="8" dy="10" stdDeviation="8" flood-color="#000" flood-opacity=".45"/>
        </filter>
      </defs>
      <use href="#cartouche" fill="var(--ink)" filter="url(#lift)"/>
      <use href="#cartouche" fill="url(#gold-rim)" transform="translate(474 466) scale(.955) translate(-474 -466)"/>
      <use href="#cartouche" fill="#5a1616" transform="translate(474 466) scale(.915) translate(-474 -466)"/>
      <use href="#cartouche" fill="url(#red-field)" transform="translate(474 466) scale(.905) translate(-474 -466)"/>
      <line x1="334" y1="551" x2="615" y2="551" stroke="var(--white)" stroke-width="1.2"/>
      <line x1="405" y1="551" x2="545" y2="551" stroke="var(--white)" stroke-width="4" stroke-dasharray="1 4" stroke-linecap="round"/>
    </svg>
    <h1 class="badge__name">VELMORINE</h1>
    <p class="badge__tagline">BEAUTY PRODUCTS</p>
  </section>
</main>
</body>
</html>
```